Circulation Rub tube and carton design

We will be launching 3 heat/soothing/circulation rubs, (intense for sports, relaxing for muscles and soothing for aches) and need a portfolio of tube and carton designs to launch with. The product name will be Velqora (Logo Required) and all 3 products will contain Arginine, which is a key feature of the product. We would like to see a bold designs but using earthy tones. Will need an information/ingredients panel on back of tube and carton. Have attached market examples of similar products.
Updates

It will need the following text included 100gm With Arginine for supporting circulation aiding in the temporary relief of Joint and Muscular Pain Joint and Muscular inflammation Stiff Joints Spains, strains, sporting injuries Mild Arthritis

Target Market(s)

there are 3 variants, they will be aimed at 3 different markets. 1. Trusk Intense - for sports 2. Trusk Relax - General population 3. Trusk Soothe - Aged population (arthritis, aches)

Requirements
Must have
• Text to be included 2 separate areas - 100gm & - With Arginine for supporting circulation aiding in the temporary relief of Joint and Muscular Pain Joint and Muscular inflammation Stiff Joints Spains, strains, sporting injuries Mild Arthritis

```html
<!DOCTYPE html>
<html lang="en">
<head>
<meta charset="utf-8">
<title>Trusk circulation rub cartons</title>
<link rel="stylesheet" href="https://fonts.googleapis.com/css2?family=PT+Serif:wght@400;700&family=Allura&display=swap">
<style>
  :root {
    --bg: #ffffff;
    --panel: #efefed;
    --ink: #3a3a3a;
    --white: #ffffff;
    --soothe-dark: #5b6680;
    --soothe-light: #93a1b4;
    --relax-dark: #586556;
    --relax-light: #a2b59e;
    --intense-dark: #8a5752;
    --intense-light: #cfb0a8;
  }
  * { margin: 0; padding: 0; box-sizing: border-box; }
  html, body { width: 1200px; height: 1200px; overflow: hidden; background: var(--bg); }
  .range {
    position: absolute; left: 50px; top: 290px;
    display: flex; gap: 40px;
  }
  .carton {
    position: relative; width: 340px; height: 600px;
    background: var(--panel);
    box-shadow: 0 1px 0 rgba(0,0,0,.06), inset 0 0 0 1px rgba(0,0,0,.05);
    font-family: "PT Serif", serif; color: var(--ink);
    text-align: center;
  }
  .soothe { --dark: var(--soothe-dark); --light: var(--soothe-light); }
  .relax { --dark: var(--relax-dark); --light: var(--relax-light); }
  .intense { --dark: var(--intense-dark); --light: var(--intense-light); }
  .brand-band {
    position: absolute; left: 110px; top: 0; width: 76px; height: 196px;
    background: var(--dark); border: 6px solid var(--light); border-top: none;
    display: flex; align-items: center; justify-content: center;
  }
  .brand-name {
    transform: rotate(-90deg); white-space: nowrap;
    color: var(--white); font-size: 28px; letter-spacing: 3px; font-weight: 400;
  }
  .product-name {
    position: absolute; top: 215px; left: 0; right: 0;
    font-size: 64px; font-weight: 700; letter-spacing: 2px; line-height: 1;
  }
  .variant {
    position: absolute; top: 262px; left: 0; right: 0;
    font-family: "Allura", cursive; font-size: 54px; color: var(--dark); line-height: 1;
  }
  .weight {
    position: absolute; top: 345px; left: 50%; transform: translateX(-50%);
    background: var(--dark); color: var(--white);
    font-size: 26px; padding: 2px 10px; line-height: 1.1;
  }
  .with { position: absolute; top: 384px; left: 0; right: 0; font-size: 20px; }
  .key-ingredient { position: absolute; top: 408px; left: 0; right: 0; font-size: 30px; }
  .rule {
    position: absolute; top: 456px; left: 70px; width: 200px; height: 6px;
    background: var(--light);
  }
  .claims {
    position: absolute; top: 474px; left: 34px; right: 34px;
    text-align: left; font-size: 11.5px; line-height: 1.45;
  }
  .claims p { text-align: justify; }
  .claims ul {
    list-style: none; margin-top: 4px; padding-left: 6px;
    border-left: 3px solid var(--dark);
  }
  .claims li::before { content: "· "; }
</style>
</head>
<body>
  <main class="range">
    <section class="carton soothe">
      <div class="brand-band"><span class="brand-name">VELQORA</span></div>
      <h1 class="product-name">TRUSK</h1>
      <div class="variant">soothe</div>
      <div class="weight">100 gm</div>
      <div class="with">with</div>
      <div class="key-ingredient">Arginine</div>
      <div class="rule"></div>
      <div class="claims">
        <p>With ARGININE for supporting circulation aiding in the temporary relief of:</p>
        <ul>
          <li>Joint and Muscular Pain</li>
          <li>Joint and Muscular inflammation</li>
          <li>Stiff Joints</li>
          <li>Spains, strains, sporting injuries</li>
          <li>Mild Arthritis</li>
        </ul>
      </div>
    </section>
    <section class="carton relax">
      <div class="brand-band"><span class="brand-name">VELQORA</span></div>
      <h1 class="product-name">TRUSK</h1>
      <div class="variant">relax</div>
      <div class="weight">100 gm</div>
      <div class="with">with</div>
      <div class="key-ingredient">Arginine</div>
      <div class="rule"></div>
      <div class="claims">
        <p>With ARGININE for supporting circulation aiding in the temporary relief of:</p>
        <ul>
          <li>Joint and Muscular Pain</li>
          <li>Joint and Muscular inflammation</li>
          <li>Stiff Joints</li>
          <li>Spains, strains, sporting injuries</li>
          <li>Mild Arthritis</li>
        </ul>
      </div>
    </section>
    <section class="carton intense">
      <div class="brand-band"><span class="brand-name">VELQORA</span></div>
      <h1 class="product-name">TRUSK</h1>
      <div class="variant">intense</div>
      <div class="weight">100 gm</div>
      <div class="with">with</div>
      <div class="key-ingredient">Arginine</div>
      <div class="rule"></div>
      <div class="claims">
        <p>With ARGININE for supporting circulation aiding in the temporary relief of:</p>
        <ul>
          <li>Joint and Muscular Pain</li>
          <li>Joint and Muscular inflammation</li>
          <li>Stiff Joints</li>
          <li>Spains, strains, sporting injuries</li>
          <li>Mild Arthritis</li>
        </ul>
      </div>
    </section>
  </main>
</body>
</html>
```